Tango Holiday Website Needs a Header Design

I'm looking for a talented designer to create an attractive header for my website: http://brightmerengue.de/. I only want a Header Design. The website and everything else should stay the same.
We will be offering vacations for people who want to come to Tenerife to learn and dance Argentine tango. There will be lessons during the day and dancing during the evening. Tenerife is a warm and sunny destination.
The header should blend in well with the background and the images. The current dimentions fo the header is 960 x 160 pixels.
I like the design on a similar website: http://velosacumbia.de/.
Here are some images on google for tango holiday that might help: http://qlnk.to/7kRw41P
I'm flexible with colours and am looking forward to your suggestions.
Tango dancers between the ages of 40 and 65

```html
<!DOCTYPE html>
<html lang="de">
<head>
<meta charset="utf-8">
<title>Bright Merengue – Tango Urlaub auf Teneriffa</title>
<link rel="stylesheet" href="https://fonts.googleapis.com/css2?family=Roboto:wght@300;400;500&display=swap">
<style>
  :root {
    --page-bg: #efefef;
    --sheet-bg: #ffffff;
    --sheet-shadow: rgba(0,0,0,0.35);
    --header-light: #fcf1cf;
    --header-mid: #f7dc97;
    --header-deep: #eec47a;
    --brand-ink: #161616;
    --tagline: #9b2a18;
    --nav-active: #1e1e1e;
    --nav-idle: #8f8f8f;
    --rule: #c9c9c9;
    --text: #3a3a3a;
    --heading: #2a2a2a;
    --dot: #111111;
    --photo-sea: #8fa7b8;
    --photo-rock: #3c3a38;
    --photo-dancers: #7c8c92;
    --photo-hall: #b88a66;
  }
  * { box-sizing: border-box; margin: 0; padding: 0; }
  html, body { width: 1200px; height: 682px; overflow: hidden; }
  body {
    background: var(--page-bg);
    font-family: "Roboto", Arial, sans-serif;
    color: var(--text);
    position: relative;
  }
  .sheet {
    position: absolute; left: 237px; top: 22px; width: 728px; height: 680px;
    background: var(--sheet-bg);
    box-shadow: 0 0 4px var(--sheet-shadow);
  }
  .site-header {
    position: absolute; left: 0; top: 0; width: 728px; height: 123px;
    background: linear-gradient(90deg, var(--header-light) 0%, var(--header-mid) 55%, var(--header-deep) 100%);
  }
  .dancer-art {
    position: absolute; left: 78px; top: 20px; width: 100px; height: 94px;
    background: linear-gradient(180deg, rgba(40,30,20,0.55), rgba(40,30,20,0.25));
    border-radius: 6px;
  }
  .brand {
    position: absolute; left: 305px; top: 24px;
    font-size: 40px; font-weight: 400; color: var(--brand-ink);
    letter-spacing: 1px; line-height: 1;
  }
  .tagline {
    position: absolute; left: 306px; top: 76px;
    font-size: 11px; font-weight: 400; color: var(--tagline);
    font-variant: small-caps; letter-spacing: 1.2px;
  }
  .main-nav {
    position: absolute; left: 0; top: 123px; width: 728px; height: 30px;
    border-bottom: 1px solid var(--rule);
    display: flex; gap: 19px; padding-left: 30px; align-items: center;
    font-size: 11.5px;
  }
  .main-nav a { text-decoration: none; color: var(--nav-idle); }
  .main-nav a.active { color: var(--nav-active); }
  .slider {
    position: absolute; left: 15px; top: 201px; width: 526px; height: 263px;
    background: linear-gradient(180deg, #dfe6ea 0%, var(--photo-sea) 45%, var(--photo-rock) 85%);
  }
  .slider-dots {
    position: absolute; left: 233px; top: 475px; display: flex; gap: 5.5px;
  }
  .slider-dots span {
    width: 8px; height: 8px; border-radius: 50%;
    border: 1.5px solid var(--dot); background: #fff;
  }
  .slider-dots span.current { background: var(--dot); }
  .content {
    position: absolute; left: 37px; top: 519px; width: 500px;
  }
  .content h1 {
    font-size: 17px; font-weight: 400; color: var(--heading); margin-bottom: 15px;
  }
  .content .quote { font-size: 11.5px; font-weight: 300; margin-bottom: 14px; }
  .content p { font-size: 11.5px; font-weight: 300; line-height: 16px; }
  .side-photo { position: absolute; left: 573px; }
  .side-photo.couple-coast {
    top: 181px; width: 133px; height: 227px;
    background: linear-gradient(180deg, #3f6f86 0%, var(--photo-dancers) 60%, #6b5a48 100%);
  }
  .side-photo.couple-hall {
    top: 439px; width: 135px; height: 123px;
    background: linear-gradient(135deg, var(--photo-hall) 0%, #d9c2a8 55%, #5c5a66 100%);
  }
  .highlights {
    position: absolute; left: 573px; top: 608px; list-style: none;
    font-size: 9.5px; line-height: 13.6px; color: var(--heading);
  }
  .highlights li::before { content: "* "; margin-right: 3px; }
</style>
</head>
<body>
  <div class="sheet">
    <header class="site-header" role="img" aria-label="Warm sunrise sky over a mountain ridge">
      <div class="dancer-art" role="img" aria-label="Silhouette of a tango dancing couple"></div>
      <div class="brand">Bright Merengue</div>
      <div class="tagline">Tango Holidays in Tenerife</div>
    </header>
    <nav class="main-nav">
      <a class="active" href="#">Homepage</a>
      <a href="#">Anbieter von Tango Reisen</a>
      <a href="#">Kontakt</a>
    </nav>
    <div class="slider" role="img" aria-label="Coastal cliffs of Tenerife with a lighthouse on a rocky point"></div>
    <div class="slider-dots"><span></span><span></span><span></span><span class="current"></span><span></span><span></span><span></span></div>
    <article class="content">
      <h1>Tango Urlaub auf Teneriffa</h1>
      <div class="quote">„Tanzen ist träumen mit den Beinen“</div>
      <p>Jeder, der bereits einmal einen Tanzkurs besucht hat, weiß, dass in diesem finnischen Sprichwort mehr als nur ein Quäntchen Wahrheit steckt. Für Außenstehende mag es so aussehen, als bewege man sich lediglich zur Musik, ein rhythmisches Miteinander der Tanzpartner, für die Tänzer ist jeder Tanz jedoch einzigartig und etwas ganz Besonderes. Die einzelnen Schritte bilden eine harmonische Abfolge an Bewegungen, jede Geste ist sorgsam durchdacht und wird voller Hingabe ausgeführt.</p>
    </article>
    <div class="side-photo couple-coast" role="img" aria-label="Tango couple dancing on rocks by the sea"></div>
    <div class="side-photo couple-hall" role="img" aria-label="Smiling couple dancing in a hall"></div>
    <ul class="highlights">
      <li>Mehr als 40 Stunden Tanz</li>
      <li>Drei Veranstaltungsorte</li>
      <li>Wunderschöne Musik</li>
      <li>Internationale DJs</li>
    </ul>
  </div>
</body>
</html>
```